I have a logo and need to design the business card and stationery.
Updates

The uploaded logo image named as GREYHAVEN CONSTRUCTION which is to be replaced to GREYHAVEN CONTRACTS. Kindly add below details and submit the designs- Company name- Greyhaven Engineering Contracts LLP Name & Post- Kunal Mehra (Designated Partner) Address- Block No.317, Wing C, Tulsi Trade Plaza, Lokhand Marg, Varun Industrial Park, Goregaon(E), Mumbai - 400 063 Contact- +91 97410 58723 Email- kunalmehra@examplemail.com Website- www.greyhavencontracts.example Contact for Letterhead- +91-22-28145597

Hi Tanvir Rahman, We are liking your Design #41927506. We have suggested some changes which are mentioned in feedback. Kindly revert with it asap to finalize this design.

Colors

Designer to choose colors to be used in the design.

```html
<!DOCTYPE html>
<html lang="en">
<head>
<meta charset="utf-8">
<title>Greyhaven Contracts Stationery</title>
<link href="https://fonts.googleapis.com/css2?family=Didact+Gothic&family=Roboto+Condensed:wght@400;700&family=Source+Sans+3:wght@600;700&display=swap" rel="stylesheet">
<style>
:root{
  --stage:#a5a8ab;
  --paper:#ffffff;
  --ink:#0b0b0b;
  --text:#3a3a3a;
  --muted:#7a7a7a;
  --faint:#eef0ef;
  --mark-dark:#2e2e2e;
  --rule:#8c8c8c;
}
*{margin:0;padding:0;box-sizing:border-box}
html,body{width:1200px;height:556px;overflow:hidden;background:var(--stage)}
body{position:relative;font-family:"Didact Gothic",sans-serif;color:var(--text)}
.sheet,.envelope,.card{position:absolute;box-shadow:2px 3px 4px rgba(0,0,0,.35)}
.sheet{top:20px;width:366px;height:518px;background:var(--paper)}
.sheet--letter{left:23px}
.sheet--blank{left:419px}
.sheet__rule{position:absolute;left:0;right:0;top:37px;border-top:1px solid var(--rule)}
.logo-box{position:absolute;left:33px;top:0;width:56px;height:67px;background:var(--ink);display:flex;align-items:center;justify-content:center}
.brand{font-family:"Roboto Condensed",sans-serif;font-weight:700;color:#fff;text-align:center;line-height:1.05;letter-spacing:.2px}
.logo-box .brand{font-size:5.2px}
.date{position:absolute;left:284px;top:22px;font-size:6.5px;color:var(--text)}
.deco{position:absolute;background:var(--faint)}
.sheet .deco{left:270px;top:42px;width:89px;height:89px}
.letter{position:absolute;left:33px;top:107px;width:300px}
.letter__to,.letter__name{font-family:"Source Sans 3",sans-serif;font-weight:700;font-size:7.5px;color:var(--ink);line-height:11px}
.letter__role{font-family:"Source Sans 3",sans-serif;font-weight:600;font-size:6.5px;color:#555;line-height:11px}
.letter__company{font-family:"Source Sans 3",sans-serif;font-weight:700;font-size:7.5px;color:var(--ink);margin-top:6px}
.letter__body p{font-size:6.6px;line-height:10.4px;margin-top:10px}
.signature{position:absolute;left:33px;top:327px;width:66px;height:39px;background:linear-gradient(90deg,#f3f3f3,#e6e6e6)}
.signoff{position:absolute;left:33px;top:378px;font-family:"Roboto Condensed",sans-serif;font-size:6px;line-height:9px}
.signoff__name{font-weight:700;color:var(--ink)}
.signoff__role{font-family:"Source Sans 3",sans-serif;font-weight:600;color:#444}
.signoff__company{color:var(--muted);letter-spacing:.3px}
.footer-block{position:absolute;left:0;top:456px;width:89px;height:57px;background:var(--ink)}
.info{position:absolute;font-family:"Roboto Condensed",sans-serif;font-size:4.3px;line-height:6.2px;color:#555}
.info__label{font-weight:700;font-size:5.2px;color:var(--ink);margin-bottom:3px}
.sheet .info--address{left:150px;top:473px;width:100px}
.sheet .info--contact{left:277px;top:473px}
.envelope{left:815px;top:82px;width:366px;height:173px;background:var(--ink)}
.envelope__window{position:absolute;left:19px;top:48px;width:124px;height:52px;background:var(--paper)}
.envelope .deco{left:287px;top:14px;width:63px;height:63px;background:var(--mark-dark)}
.envelope__brand{position:absolute;left:19px;top:139px;font-size:4.6px}
.envelope__divider{position:absolute;left:69px;top:136px;height:24px;border-left:1px solid #555}
.envelope__company{position:absolute;left:79px;top:136px;font-size:6.5px;line-height:8px;color:#6e6e6e}
.envelope .info{color:#777}
.envelope .info__label{color:#fff}
.envelope .info--address{left:190px;top:135px;width:95px}
.envelope .info--contact{left:289px;top:135px}
.card{top:329px;width:149px;height:95px}
.card--dark{left:815px;background:var(--ink)}
.card--light{left:990px;background:var(--paper)}
.card__company{position:absolute;left:6px;top:12px;font-family:"Source Sans 3",sans-serif;font-weight:700;font-size:8.3px;line-height:9.6px;color:#474747}
.card--dark .deco{left:105px;top:9px;width:39px;height:39px;background:var(--mark-dark)}
.card__divider{position:absolute;left:6px;top:62px;width:81px;border-top:1px solid #555}
.card__address{position:absolute;left:6px;top:67px;width:86px;font-family:"Roboto Condensed",sans-serif;font-size:4.2px;line-height:6px;color:#bbb}
.card__name{position:absolute;left:6px;top:17px;font-family:"Source Sans 3",sans-serif;font-weight:700;font-size:8px;color:var(--ink)}
.card__role{position:absolute;left:6px;top:27px;font-family:"Source Sans 3",sans-serif;font-weight:600;font-size:5.5px;color:#555}
.card__contacts{position:absolute;left:6px;top:55px;width:65px;list-style:none;font-size:4.3px;color:#555}
.card__contacts li{padding:1.5px 0;border-bottom:1px solid #ddd;height:10px}
.card__contacts li:last-child{border-bottom:none}
.card--light .deco{left:105px;top:9px;width:38px;height:38px}
.card__brand{position:absolute;left:106px;top:62px;color:var(--ink);font-size:4.6px}
</style>
</head>
<body>

<section class="sheet sheet--letter">
  <div class="logo-box"><span class="brand">GREYHAVEN<br>CONTRACTS</span></div>
  <div class="sheet__rule"></div>
  <div class="date">Date......---/--/----</div>
  <div class="deco"></div>
  <div class="letter">
    <div class="letter__to">To,</div>
    <div class="letter__name">KUNAL MEHRA</div>
    <div class="letter__role">(Designated Partner)</div>
    <div class="letter__company">GREYHAVEN ENGINEERING CONTRACTS LLP</div>
    <div class="letter__body">
      <p>Lorem ipsum dolor sit amet, consectetur adipiscing elit, sed do eiusmod tempor incididunt ut labore et dolore magna aliqua. Ut enim ad minim veniam, quis nostrud exercitation ullamco laboris nisi ut aliquip ex ea commodo consequat. Duis aute irure dolor in reprehenderit in voluptate velit esse cillum dolore eu fugiat nulla pariatur. Excepteur sint occaecat cupidatat non proident, sunt in culpa qui officia deserunt mollit anim id est laborum.</p>
      <p>The standard chunk of Lorem Ipsum used since the 1500s is reproduced below for those interest the 1914 translation by H. Rackham.</p>
      <p>The standard chunk of Lorem Ipsum used since the 1500s is reproduced below for those interested. Sections 1.10.32 and 1.10.33 from "de Finibus Bonorum et Malorum" by Cicero are also reproduced in their exact original form, accompanied by English versions from the 1914 translation by H. Rackham.</p>
    </div>
  </div>
  <div class="signature" role="img" aria-label="Handwritten signature"></div>
  <div class="signoff">
    <div class="signoff__name">KUNAL MEHRA</div>
    <div class="signoff__role">(Designated Partner)</div>
    <div class="signoff__company">GREYHAVEN ENGINEERING CONTRACTS LLP</div>
  </div>
  <div class="footer-block"></div>
  <div class="info info--address">
    <div class="info__label">ADDRESS</div>
    Block No.317, Wing C, Tulsi Trade Plaza,<br>Lokhand Marg, Varun Industrial Park,<br>Goregaon(E), Mumbai - 400 063
  </div>
  <div class="info info--contact">
    <div class="info__label">CONTACT</div>
    +91-22-28145597<br>kunalmehra@examplemail.com<br><b>www.greyhavencontracts.example</b>
  </div>
</section>

<section class="sheet sheet--blank">
  <div class="logo-box"><span class="brand">GREYHAVEN<br>CONTRACTS</span></div>
  <div class="sheet__rule"></div>
  <div class="date">Date......---/--/----</div>
  <div class="deco"></div>
  <div class="footer-block"></div>
  <div class="info info--address">
    <div class="info__label">ADDRESS</div>
    Block No.317, Wing C, Tulsi Trade Plaza,<br>Lokhand Marg, Varun Industrial Park,<br>Goregaon(E), Mumbai - 400 063
  </div>
  <div class="info info--contact">
    <div class="info__label">CONTACT</div>
    +91-22-28145597<br>kunalmehra@examplemail.com<br><b>www.greyhavencontracts.example</b>
  </div>
</section>

<section class="envelope">
  <div class="envelope__window"></div>
  <div class="deco"></div>
  <span class="brand envelope__brand">GREYHAVEN<br>CONTRACTS</span>
  <div class="envelope__divider"></div>
  <div class="envelope__company">Greyhaven Engineering<br>Contracts LLP</div>
  <div class="info info--address">
    <div class="info__label">ADDRESS</div>
    Block No.317, Wing C, Tulsi Trade Plaza,<br>Lokhand Marg, Varun Industrial Park,<br>Goregaon(E), Mumbai - 400 063
  </div>
  <div class="info info--contact">
    <div class="info__label">CONTACT</div>
    +91-22-28145597<br>kunalmehra@examplemail.com<br>www.greyhavencontracts.example
  </div>
</section>

<section class="card card--dark">
  <div class="card__company">Greyhaven<br>Engineering<br>Contracts<br>LLP</div>
  <div class="deco"></div>
  <div class="card__divider"></div>
  <div class="card__address">Block No.317, Wing C, Tulsi Trade Plaza, Lokhand Marg, Varun Industrial Park, Goregaon(E), Mumbai - 400 063</div>
</section>

<section class="card card--light">
  <div class="card__name">KUNAL MEHRA</div>
  <div class="card__role">(Designated Partner)</div>
  <div class="deco"></div>
  <ul class="card__contacts">
    <li>+91 97410 58723</li>
    <li>kunalmehra@examplemail.com</li>
    <li>www.greyhavencontracts.example</li>
  </ul>
  <span class="brand card__brand">GREYHAVEN<br>CONTRACTS</span>
</section>

</body>
</html>
```